Create a new business card

I’m looking to update my business card to make it match the rest of my brand. I will include my current website as well as what my vehicle designs look like, etc..
What my business currently services
Weekly maintenance pool openings / closings
Equipment repair, including pumps, heaters, salt systems, filters, etc.
We install automatic covers and maintain them as well as provide preventative maintenance

I would like to include my name.
Darren Holcott.
My title
Owner
My email
Darren@tidewellnx.com
4015867120
Www.tidewellnx.com

```html
<!DOCTYPE html>
<html lang="en">
<head>
<meta charset="utf-8">
<title>Tidewell Pool Service – Business Card</title>
<link rel="stylesheet" href="https://fonts.googleapis.com/css2?family=Montserrat:wght@400;500;700&family=Roboto+Condensed:wght@700&display=swap">
<style>
  :root {
    --canvas: #e6e8ec;
    --white: #ffffff;
    --navy: #2b3a6e;
    --sky: #36b6e8;
    --orange: #e8602a;
    --ink: #0d0f1a;
    --shadow: rgba(20, 28, 50, 0.22);
  }
  * { box-sizing: border-box; margin: 0; padding: 0; }
  html, body { width: 1200px; height: 900px; overflow: hidden; }
  body {
    background: var(--canvas);
    font-family: "Montserrat", Arial, sans-serif;
    position: relative;
  }
  .card {
    position: absolute;
    border-radius: 22px;
    overflow: hidden;
    background: var(--white);
    box-shadow: 0 14px 32px var(--shadow);
  }
  .card-art { position: absolute; inset: 0; width: 100%; height: 100%; display: block; }

  /* Front card (portrait) */
  .card-front { left: 110px; top: 150px; width: 350px; height: 600px; }
  .brand-mark {
    position: absolute;
    display: flex; align-items: center; gap: 10px;
    color: var(--navy);
    font-weight: 700;
    white-space: nowrap;
  }
  .brand-dot {
    width: 30px; height: 30px; border-radius: 50%;
    background: var(--sky); flex: none;
  }
  .card-front .brand-mark { left: 38px; top: 110px; font-size: 22px; line-height: 1.15; }
  .person { position: absolute; left: 40px; top: 396px; color: var(--ink); white-space: nowrap; }
  .person-name { font-size: 28px; font-weight: 700; letter-spacing: 0.2px; line-height: 1.15; }
  .person-title { font-size: 15px; font-weight: 400; margin-top: 2px; }
  .contact-list { position: absolute; left: 40px; top: 478px; list-style: none; color: var(--ink); }
  .contact-item { display: flex; align-items: center; gap: 12px; font-size: 16.5px; font-weight: 500; margin-bottom: 9px; white-space: nowrap; }
  .contact-icon { width: 15px; height: 15px; flex: none; fill: var(--ink); }

  /* Back card (landscape) */
  .card-back { left: 560px; top: 150px; width: 560px; height: 330px; }
  .card-back .brand-mark { right: 60px; top: 40px; font-size: 20px; }
  .services {
    position: absolute; left: 34px; top: 128px; width: 500px;
    color: var(--white);
    font-family: "Roboto Condensed", "Arial Narrow", sans-serif;
    font-weight: 700;
  }
  .services-heading { font-size: 21px; letter-spacing: 0.4px; text-transform: uppercase; margin-bottom: 8px; padding-left: 60px; }
  .services-list { list-style: none; font-size: 15px; line-height: 1.35; }
  .services-list li { padding-left: 14px; position: relative; }
  .services-list li::before { content: "•"; position: absolute; left: 0; }
  .services-list .indent { padding-left: 86px; }
  .services-list .indent::before { left: 72px; }
</style>
</head>
<body>

<section class="card card-front" aria-label="Business card front">
  <svg class="card-art" viewBox="0 0 350 600" preserveAspectRatio="none" aria-hidden="true">
    <rect width="350" height="600" fill="var(--white)"/>
    <path d="M0,345 C150,330 275,260 320,120 L350,120 L350,600 L0,600 Z" fill="var(--navy)"/>
    <path d="M0,372 C170,352 300,300 350,190 L350,600 L0,600 Z" fill="var(--sky)"/>
    <path d="M0,345 C150,332 262,300 308,220 C270,315 160,356 0,372 Z" fill="var(--orange)"/>
  </svg>
  <div class="brand-mark">
    <span class="brand-dot"></span>
    <span>Tidewell<br>Pool Service</span>
  </div>
  <div class="person">
    <p class="person-name">Darren Holcott.</p>
    <p class="person-title">Managing Director</p>
  </div>
  <ul class="contact-list">
    <li class="contact-item">
      <svg class="contact-icon" viewBox="0 0 24 24" aria-hidden="true"><path d="M6.6 10.8a15.1 15.1 0 0 0 6.6 6.6l2.2-2.2a1 1 0 0 1 1-.25 11.4 11.4 0 0 0 3.6.57 1 1 0 0 1 1 1V20a1 1 0 0 1-1 1A17 17 0 0 1 3 4a1 1 0 0 1 1-1h3.5a1 1 0 0 1 1 1c0 1.25.2 2.45.57 3.57a1 1 0 0 1-.25 1z"/></svg>
      <span>4015867120</span>
    </li>
    <li class="contact-item">
      <svg class="contact-icon" viewBox="0 0 24 24" aria-hidden="true"><path d="M2 5h20v14H2z M3.5 6.5 12 13l8.5-6.5v-.2H3.5z" fill-rule="evenodd"/></svg>
      <span>Darren@tidewellnx.com</span>
    </li>
    <li class="contact-item">
      <svg class="contact-icon" viewBox="0 0 24 24" aria-hidden="true"><circle cx="12" cy="12" r="10"/><path d="M2 12h20M12 2c3 3 3 17 0 20M12 2c-3 3-3 17 0 20" stroke="var(--sky)" stroke-width="1.4" fill="none"/></svg>
      <span>Www.tidewellnx.com</span>
    </li>
  </ul>
</section>

<section class="card card-back" aria-label="Business card back">
  <svg class="card-art" viewBox="0 0 560 330" preserveAspectRatio="none" aria-hidden="true">
    <rect width="560" height="330" fill="var(--white)"/>
    <rect y="100" width="560" height="230" fill="var(--navy)"/>
  </svg>
  <div class="brand-mark">
    <span class="brand-dot"></span>
    <span>Tidewell Pool Service</span>
  </div>
  <div class="services">
    <p class="services-heading">What my business currently services</p>
    <ul class="services-list">
      <li class="indent">Weekly maintenance pool openings / closings</li>
      <li>Equipment repair, including pumps, heaters, salt systems, filters, etc.</li>
      <li>We install automatic covers and maintain them as well as provide preventative maintenance</li>
    </ul>
  </div>
</section>

</body>
</html>
```